TOPページのイメージを作成していただきたいです。
女性が入りやすく、親しみやすい色使いとフォントで、
カテゴリのボタンはアイコン等を使い、やわらかい印象を与えたい
※アイコンを指定しているわけではありません。

商品にカラフルなものが多くなりやすいので、全体的な色バランスはシンプルなカラーでお願いします。
サイドバナーとメインに上記スクールをターゲットとしたカテゴリに飛ぶためのバナー用意してほしいです。
近いサイトイメージは合わせて送らせていただきます。
スマートフォンでも表示させやすいレイアウトを希望します。
Zorvaneのショッピングに関しては、Zorvaneプリズムを契約予定です。
また、今回はトップページだけですが、契約させて頂いた方には商品ページなどサブページも依頼する可能性が高いです

-------------------
項目について
-------------------
※スプレッドシート参照
https://sheets.plumaria-files.com/s/7QxLk2PwZt9RvMnB4cYdHe8JfUa3Gs6KiWoN1bTq/view?share=link
■ヘッダー
検索窓、お支払いについて、送料、お届けについて、返品、交換、保証について、会社概要、プライバシーポリシー、お問い合わせ、よくある質問
■フッター
店舗内簡易情報として、イメージ画像のような下記の内容を用意する予定で、記述箇所のデザインを用意してください
送料について、支払い方法について、手数料、納期、キャンセルについて、商品の在庫について
■カテゴリ
カテゴリは、別紙の資料の通りです。
大カテゴリがメイン、中に小カテゴリがあります。

■写真資料
https://store.plumaria-files.com/f/4kXw9RtLmQ2zPbVn8HcJd5YsGa/open?share=link

■サイト見本イメージ
https://mall.brimwelt.jp/tessarino/
https://loom-harbor.com/
https://ec.pinefeld.jp/
https://www.mirusato.co.jp/shop/c/c10/
https://www.webshop.velmo-quarry.com/
https://studio.quillop.net/
サイトの色合いや雰囲気に近いサイトになります。
1ページ
赤系、黄・オレンジ系、茶系
• イラストレーター形式 (.ai)
幅1250px程度
※Zorvaneショップのバナーサイズを考慮しています。
場合によってはその他のページもお願いする可能性があります。
もう少し提案数を頂きたいため、5月13日(金)までコンペの延長をいたします。

今回選ばせていただきました理由は
・商品を邪魔しないシンプルさ
・Zorvaneショップに落とし込んだ時に差異が生まれにくい点
・全体的な色使い
を中心に選ばせていただきました。
非常にあたたかく、親しみやすいデザインで作成いただきましたので、こちらに決定させていただきました。

今回いただきました提案はどれも素晴らしく、選考は非常に悩みました。
冒険するか、無難なデザインにするか、また、その中でもどれがいいか、かなり悩みまして、選ばれなかったデザインも、最後までの残ったデザインがいくつかございました。
本当に皆様ご提案ありがとうございました。
また次の機会がございましたら、是非よろしくお願いします。

```html
<!DOCTYPE html>
<html lang="ja">
<head>
<meta charset="utf-8">
<title>ふわりや。 ハンドメイドアイテム専門店</title>
<link rel="stylesheet" href="https://fonts.googleapis.com/css2?family=M+PLUS+Rounded+1c:wght@400;500;700;800&display=swap">
<style>
:root{
  --lavender:#c7b6dc;
  --lavender-soft:#e9e3f1;
  --lavender-deep:#8f7bb0;
  --ink:#3d3a40;
  --ink-soft:#6c6870;
  --line:#d9d4de;
  --paper:#ffffff;
  --cream:#f7f4ee;
}
*{box-sizing:border-box;margin:0;padding:0}
html,body{width:752px;height:1200px;overflow:hidden;background:var(--paper)}
body{position:relative;font-family:"M PLUS Rounded 1c",sans-serif;color:var(--ink);font-size:9px}
.abs{position:absolute}

/* header */
.shop-tag{left:70px;top:12px;font-size:8px;color:var(--ink-soft)}
.logo{left:70px;top:24px;font-size:24px;font-weight:700;letter-spacing:1px;display:flex;align-items:center;gap:6px}
.logo-dot{width:8px;height:8px;border-radius:50%;background:var(--lavender-deep)}
.logo-sub{left:72px;top:55px;font-size:7px;color:var(--ink-soft)}
.search{left:255px;top:36px;width:140px;height:22px;border:1px solid var(--line);border-radius:3px;display:flex;justify-content:flex-end;align-items:center;padding-right:6px}
.header-links{left:415px;top:28px;width:270px;display:grid;grid-template-columns:repeat(3,1fr);row-gap:14px;font-size:7.5px;color:var(--ink-soft)}
.icon-row{left:70px;top:72px;display:flex;gap:9px;align-items:center}
.sns-dot{width:14px;height:14px;border-radius:50%;border:1.5px solid var(--ink)}

/* nav */
.global-nav{left:70px;top:96px;width:612px;height:20px;background:var(--lavender);display:flex}
.global-nav a{flex:1;text-align:center;line-height:20px;color:#fff;font-size:9px;font-weight:500;text-decoration:none}

/* hero */
.hero{left:0;top:118px;width:752px;height:122px;display:flex;gap:4px}
.hero-slide{flex:1}
.hero-arrow{top:168px;width:20px;height:20px;border-radius:50%;background:rgba(0,0,0,.35);display:flex;align-items:center;justify-content:center}
.dots{left:0;width:752px;top:250px;display:flex;justify-content:center;gap:10px}
.dots span{width:5px;height:5px;border-radius:50%;background:var(--line)}
.dots span.on{background:var(--lavender-deep)}
.tagline{left:0;width:752px;top:264px;text-align:center;font-size:10px;line-height:16px;color:var(--ink)}

/* sidebar */
.sidebar{left:70px;top:326px;width:132px}
.side-title{display:flex;align-items:center;gap:5px;font-size:9px;font-weight:700;padding-bottom:6px;border-bottom:2px solid var(--lavender)}
.side-title i{width:10px;height:10px;border-radius:50%;background:var(--lavender-deep);display:block}
.side-list{list-style:none;margin-bottom:18px}
.side-list li{font-size:7.5px;height:25px;line-height:25px;padding-left:10px;border-bottom:1px solid var(--line)}
.sns-space{width:112px;height:112px;margin-left:10px;border:1px solid var(--line);display:flex;flex-direction:column;justify-content:center;align-items:center;font-size:8px;gap:4px}

/* main */
.banner{left:225px;width:430px;height:122px;display:flex;align-items:center;justify-content:center}
.banner-title{font-size:34px;font-weight:800;color:#fff;letter-spacing:2px;text-shadow:0 0 8px rgba(120,100,140,.5)}
.event{top:343px;background:linear-gradient(90deg,#e7d9cc 0%,#f0e4e8 45%,#d8c8e2 100%)}
.starter{top:491px;background:linear-gradient(90deg,#b9a690 0%,#ece6da 40%,#ece6da 70%,#c9ae86 100%)}
.starter .banner-title{color:#f4ef7a;text-shadow:0 0 8px rgba(90,80,60,.5)}
.howto{left:225px;top:638px;width:430px;text-align:center}
.howto h2{font-size:30px;font-weight:800;letter-spacing:3px;line-height:34px}
.howto p{font-size:9px;color:var(--ink-soft)}
.cards{left:236px;top:717px;width:410px;display:grid;grid-template-columns:1fr 1fr;column-gap:28px;row-gap:18px}
.card{height:128px;position:relative;display:flex;align-items:center;justify-content:center}
.card-label{text-align:center;color:var(--ink)}
.card-label em{display:block;font-style:normal;font-size:22px;font-weight:500;color:var(--lavender-deep);line-height:22px}
.card-label span{display:inline-block;background:rgba(255,255,255,.85);font-size:11px;font-weight:700;padding:3px 8px;margin-top:3px}
.cut{background:linear-gradient(135deg,#f3d77b,#9dc0dd 60%,#f0eee8)}
.iron{background:linear-gradient(135deg,#9c958d,#d7d2cb 55%,#eeeae3)}
.keep{background:linear-gradient(135deg,#f2eee9,#e4dfea 60%,#f6f3ef)}
.attention{background:linear-gradient(135deg,#ddd3c7,#f1ece4 55%,#cfc4b6)}

/* footer */
.footer{left:0;top:1030px;width:752px;height:170px;background:var(--lavender-soft)}
.pay-cards{left:72px;top:1074px;display:grid;grid-template-columns:repeat(3,24px);gap:5px}
.pay-cards span{height:15px;border-radius:2px;background:#fff;border:1px solid var(--line)}
.footer-col{font-size:6.5px;line-height:11px;color:var(--ink-soft)}
.footer-col b{display:block;color:var(--ink);font-size:7.5px}
.footer-links{left:502px;top:1052px;display:grid;grid-template-columns:88px 88px;row-gap:10px;font-size:7px;color:var(--ink-soft)}
</style>
</head>
<body>

<header>
  <p class="abs shop-tag">ハンドメイドアイテム専門店</p>
  <div class="abs logo">ふわりや。<span class="logo-dot"></span></div>
  <p class="abs logo-sub">hand made shop</p>
  <div class="abs search">
    <svg width="10" height="10" viewBox="0 0 10 10"><circle cx="4" cy="4" r="3" fill="none" stroke="#3d3a40" stroke-width="1.2"/><line x1="6.2" y1="6.2" x2="9.2" y2="9.2" stroke="#3d3a40" stroke-width="1.2"/></svg>
  </div>
  <nav class="abs header-links">
    <span>お支払いについて</span><span>送料・お届けについて</span><span>返品・交換・保証について</span>
    <span>会社概要</span><span>プライバシーポリシー</span><span>お問い合わせ ／ よくある質問</span>
  </nav>
  <div class="abs icon-row">
    <span class="sns-dot"></span><span class="sns-dot"></span>
    <svg width="16" height="14" viewBox="0 0 16 14"><path d="M1 1h3l2 8h8l1.5-6H5" fill="none" stroke="#3d3a40" stroke-width="1.3"/><circle cx="7" cy="12" r="1.3" fill="#3d3a40"/><circle cx="13" cy="12" r="1.3" fill="#3d3a40"/></svg>
  </div>
</header>

<nav class="abs global-nav">
  <a>おすすめアイテム</a><a>人気ランキング</a><a>新着アイテム</a><a>セール品</a>
</nav>

<section class="abs hero">
  <div class="hero-slide" style="background:linear-gradient(135deg,#d8d3cc,#eeeae4)" role="img" aria-label="プリントTシャツの商品写真"></div>
  <div class="hero-slide" style="background:linear-gradient(135deg,#8e9a6f,#c9b9a0)" role="img" aria-label="オリジナルプリントのトートバッグ写真"></div>
  <div class="hero-slide" style="background:linear-gradient(135deg,#b88a5c,#e9e4dc)" role="img" aria-label="カラフルなトートバッグ並びの写真"></div>
  <div class="hero-slide" style="background:linear-gradient(135deg,#e7e3dd,#8aa0b8)" role="img" aria-label="デニム風の小物の写真"></div>
</section>
<div class="abs hero-arrow" style="left:150px"><svg width="8" height="10"><path d="M6 1L2 5l4 4" fill="none" stroke="#fff" stroke-width="1.6"/></svg></div>
<div class="abs hero-arrow" style="left:582px"><svg width="8" height="10"><path d="M2 1l4 4-4 4" fill="none" stroke="#fff" stroke-width="1.6"/></svg></div>
<div class="abs dots"><span class="on"></span><span></span><span></span><span></span></div>
<p class="abs tagline">モノヅクリが楽しくなる！　初めてでも簡単に自分だけのアイテムが作れます！<br>イベントなどでも楽しめるコンテンツを豊富にご提供します</p>

<aside class="abs sidebar">
  <h3 class="side-title"><i></i>カテゴリー覧</h3>
  <ul class="side-list">
    <li>裁縫用品</li><li>染色・ペイント・プリント</li><li>加工機械</li><li>刺繍素材</li>
    <li>加工素材</li><li>カット用具</li><li>布素材</li><li>梱包</li>
    <li>Tシャツ作成</li><li>バッグ作成</li><li>アイロンシート＆作成</li>
  </ul>
  <h3 class="side-title"><i></i>セット商品</h3>
  <ul class="side-list">
    <li>イベントキット</li><li>スタートキット</li>
  </ul>
  <div class="sns-space"><span>SNS スペース</span><span>Timeline 欄</span></div>
</aside>

<main>
  <div class="abs banner event" role="img" aria-label="工作を楽しむ子どもの写真のバナー"><span class="banner-title">イベント特集</span></div>
  <div class="abs banner starter" role="img" aria-label="バッグと道具セットの写真のバナー"><span class="banner-title">スタートキット</span></div>

  <div class="abs howto"><h2>HOW TO</h2><p>初めての方向けコンテンツ</p></div>

  <div class="abs cards">
    <div class="card cut" role="img" aria-label="カッティングシートの写真"><div class="card-label"><em>cut</em><span>シートのカット方法に<br>ついて</span></div></div>
    <div class="card iron" role="img" aria-label="アイロン作業の写真"><div class="card-label"><em>iron</em><span>シート加工の仕方<br>（アイロン編）</span></div></div>
    <div class="card keep" role="img" aria-label="たたまれた衣類の写真"><div class="card-label"><em>keep</em><span>長く持たせるには</span></div></div>
    <div class="card attention" role="img" aria-label="プリント加工品の写真"><div class="card-label"><em>attention</em><span>加工品の注意点</span></div></div>
  </div>
</main>

<footer class="abs footer"></footer>
<div class="abs pay-cards"><span></span><span></span><span></span><span></span><span></span><span></span></div>
<div class="abs footer-col" style="left:160px;top:1048px;width:150px">
  <b>送料について</b>全国一律の送料でお届けします<br><br>
  <b>支払い方法について</b>各種カード・振込に対応しております<br><br>
  <b>手数料</b>お支払い方法により異なります
</div>
<div class="abs footer-col" style="left:330px;top:1048px;width:150px">
  <b>納期</b>ご注文から3営業日以内に発送<br><br>
  <b>キャンセルについて</b>発送前までご対応いたします<br><br>
  <b>商品の在庫について</b>在庫は実店舗と共有しております
</div>
<nav class="abs footer-links">
  <span>会社概要</span><span>お問い合わせ</span>
  <span>プライバシーポリシー</span><span>よくある質問</span>
  <span>お支払いについて</span><span>返品・交換について</span>
</nav>

</body>
</html>
```